Photo-Video Combo Package Flyer

Need to create a flyer to showcase a combo package featuring photography and videography from two separate companies. I need an 8 1/2 X 11 flyer in .psd so I can make changes as needed as well as all fonts
Target Market(s)
Brides & Grooms
Industry/Entity Type
Wedding Photography
Requirements
Must have
- see word doc
Nice to have
- please visit websites for inspiration
- https://quietharborimages.com/
- www.kqbrt.com

```html
<!DOCTYPE html>
<html lang="en">
<head>
<meta charset="utf-8">
<title>Photo-Video Combo Package Flyer</title>
<link rel="stylesheet" href="https://fonts.googleapis.com/css2?family=Bebas+Neue&family=Montserrat:wght@300;400;500;700&display=swap">
<style>
  :root {
    --stage: #232323;
    --charcoal: #3d3d3f;
    --slate: #5f5f61;
    --slate-light: #6b6b6d;
    --paper: #ffffff;
    --mist: #ececec;
    --card: #f2f2f2;
    --ink: #333333;
    --ink-soft: #6a6a6a;
    --accent: #9a5a4e;
  }
  * { box-sizing: border-box; margin: 0; padding: 0; }
  html, body { width: 1200px; height: 1200px; overflow: hidden; }
  body { background: var(--stage); font-family: "Montserrat", sans-serif; }

  .flyer {
    position: absolute; left: 154px; top: 23px;
    width: 891px; height: 1154px;
    background: var(--paper); overflow: hidden;
  }
  .hero {
    position: absolute; left: 0; top: 0; width: 891px; height: 452px;
    background: linear-gradient(180deg, #7d6f8e 0%, #c79a8f 35%, #e8a96e 48%, #4f4a5a 55%, #6b4f3f 75%, #3a2a22 100%);
  }
  .price-tag {
    position: absolute; left: 647px; top: 0; width: 231px; height: 198px;
    color: var(--paper); text-align: center; font-family: "Bebas Neue", sans-serif;
  }
  .price-tag svg { position: absolute; inset: 0; }
  .price-tag .label { position: relative; padding-top: 28px; font-size: 25px; letter-spacing: 0.2px; }
  .price-tag .amount { position: relative; font-size: 78px; line-height: 0.95; }
  .price-tag .savings { position: relative; font-size: 23px; }

  .badge {
    position: absolute; left: 82px; top: 122px; width: 208px; height: 208px;
    border-radius: 50%; background: var(--paper);
  }
  .badge-inner {
    position: absolute; inset: 12px; border-radius: 50%; background: var(--charcoal);
    color: var(--paper); display: flex; flex-direction: column; align-items: center; justify-content: center;
  }
  .badge-text { transform: rotate(-22deg); text-align: center; line-height: 1; }
  .badge-text .plus { font-size: 17px; font-weight: 500; display: block; margin-left: -40px; }
  .badge-text .save { font-size: 34px; font-weight: 500; display: block; margin: 2px 0; }
  .badge-text .off { font-size: 16px; font-weight: 400; display: block; }

  .intro {
    position: absolute; left: 0; top: 458px; width: 891px; height: 142px;
    background: var(--charcoal); color: var(--paper);
    padding: 35px 46px 0; font-size: 13.4px; line-height: 1.35;
  }
  .intro p + p { margin-top: 14px; }

  .gallery { position: absolute; left: 0; top: 608px; width: 891px; height: 139px; }

  .services {
    position: absolute; left: 0; top: 747px; width: 891px; height: 339px;
    background: linear-gradient(90deg, #e4e4e4 0%, #f4f4f4 50%, #ffffff 100%);
  }
  .card {
    position: absolute; top: -5px; width: 348px; height: 304px;
    background: var(--card); box-shadow: 0 2px 6px rgba(0,0,0,0.18);
  }
  .card.photo { left: 80px; }
  .card.video { left: 462px; }
  .card h3 { font-weight: 400; font-size: 17.5px; color: var(--ink); text-align: center; padding-top: 5px; }
  .card .brand {
    height: 66px; display: flex; align-items: center; justify-content: center; gap: 10px;
    font-size: 22px; font-weight: 500; color: var(--accent); letter-spacing: 0.5px;
  }
  .card.video .brand { color: #2c3e7a; }
  .brand .dot { width: 12px; height: 12px; border-radius: 50%; background: currentColor; }
  .card ul { list-style: none; padding: 4px 18px 0 30px; color: var(--ink-soft); font-size: 13.3px; font-weight: 300; line-height: 1.5; }
  .card li { position: relative; padding-left: 11px; }
  .card li::before { content: "•"; position: absolute; left: 0; }
  .card .retail {
    position: absolute; left: 0; bottom: 0; width: 100%; height: 50px;
    background: var(--slate-light); color: var(--paper);
    font-size: 22px; text-align: center; line-height: 50px;
  }

  .cta {
    position: absolute; left: 114px; top: 1064px; width: 664px; height: 42px;
    border-radius: 21px; background: var(--charcoal); color: var(--paper);
    font-size: 19px; font-weight: 700; text-align: center; line-height: 42px; z-index: 2;
    letter-spacing: -0.2px;
  }
  .contact {
    position: absolute; left: 0; top: 1086px; width: 891px; height: 68px;
    display: flex; color: var(--paper); font-size: 17px;
  }
  .contact .side { display: flex; align-items: center; padding-top: 14px; }
  .contact .left { width: 446px; background: var(--slate-light); padding-left: 25px; }
  .contact .right { flex: 1; background: var(--slate); padding-left: 86px; }
  .contact .sep { margin: 0 12px; opacity: 0.6; }
</style>
</head>
<body>
<main class="flyer">
  <section class="hero" role="img" aria-label="Wedding couple embracing on a ship deck at sunset over the ocean"></section>

  <div class="price-tag">
    <svg width="231" height="198" viewBox="0 0 231 198"><polygon points="0,0 231,0 231,176 115.5,198 0,176" fill="#3d3d3f"/></svg>
    <div class="label">Photo Video Combo Price</div>
    <div class="amount">$2999</div>
    <div class="savings">($750 Savings)</div>
  </div>

  <div class="badge">
    <div class="badge-inner">
      <div class="badge-text">
        <span class="plus">PLUS</span>
        <span class="save">SAVE 10%</span>
        <span class="off">off any upgrades</span>
      </div>
    </div>
  </div>

  <section class="intro">
    <p>The Photo-Video combo package is the best way to hire your Photographer and videographer.&nbsp; Both companies are highly rated by Vow Guide and Aisle Review as well as recommended by the area’s top wedding venues.</p>
    <p>When your photographer and videographer are working together your wedding day will run smoothly, so you can just enjoy yourself and have fun!</p>
  </section>

  <svg class="gallery" width="891" height="139" viewBox="0 0 891 139">
    <defs>
      <linearGradient id="garden" x1="0" y1="0" x2="0" y2="1"><stop offset="0" stop-color="#3f5a3a"/><stop offset="1" stop-color="#1e2a1c"/></linearGradient>
      <linearGradient id="marina" x1="0" y1="0" x2="0" y2="1"><stop offset="0" stop-color="#c9a98a"/><stop offset="0.55" stop-color="#6d6a6c"/><stop offset="1" stop-color="#2e2c30"/></linearGradient>
      <linearGradient id="beach" x1="0" y1="0" x2="0" y2="1"><stop offset="0" stop-color="#f2a45a"/><stop offset="0.55" stop-color="#e8b98a"/><stop offset="1" stop-color="#5e7c95"/></linearGradient>
    </defs>
    <g role="img" aria-label="Couple in a garden at dusk"><polygon points="0,0 290,0 270,139 0,139" fill="url(#garden)"/></g>
    <g role="img" aria-label="Couple standing on a marina dock at sunset"><polygon points="298,0 590,0 570,139 278,139" fill="url(#marina)"/></g>
    <g role="img" aria-label="Couple kissing on a beach at sunset"><polygon points="597,0 891,0 891,139 577,139" fill="url(#beach)"/></g>
  </svg>

  <section class="services">
    <article class="card photo">
      <h3>Photography provided by</h3>
      <div class="brand"><span class="dot"></span>Quiet Harbor Images</div>
      <ul>
        <li>1 Hr Engagement Shoot</li>
        <li>One photographer up to 7 hours on location for wedding</li>
        <li>High Resolution, Edited digital images</li>
        <li>Images professionally edited in house</li>
        <li>Beautiful online gallery to download from</li>
        <li>Print release to print at the lab of your choice</li>
      </ul>
      <div class="retail">Normal Retail Price $2450</div>
    </article>
    <article class="card video">
      <h3>Videography provided by</h3>
      <div class="brand"><span class="dot"></span>Kestrel Quay Video</div>
      <ul>
        <li>Up To 6 Hours of Coverage</li>
        <li>Documentary Style Video Edit 60-90 Minutes</li>
        <li>Edited Background Music</li>
        <li>A Cinematic highlight Recap 3-4 minutes</li>
        <li>3 Personalized DVDs</li>
      </ul>
      <div class="retail">Normal retail Price $1299</div>
    </article>
  </section>

  <div class="cta">CONTACT US TO LEARN MORE AND SCHEDULE A CONSULTATION.</div>

  <footer class="contact">
    <div class="side left">941-555-0142<span class="sep">|</span>quietharborimages.com</div>
    <div class="side right">941-555-0187<span class="sep">|</span>www.kqbrt.com</div>
  </footer>
</main>
</body>
</html>
```